Tollo is the place for Used Car Inspections

Tollo ONLY sells Used Car Inspections.

We need a website that tells that story simply.

Please be original and don't just copy my mockup. I'm not a designer.

Reason: Too few designers(<10)...too many weak designs(>80). I have subsequently revised my brief, uploaded more defined mockup and have tried to inspire some originality. I have also invited add designs, some who have declined. Any suggestions. Any suggestions?

Reason: Still waiting on original designs

Target Market(s)

Car Buyers

Industry/Entity Type

Used Car

Logo Text

Tollo

Number of Pages Required

5+ page

Font styles to use
Sans Serif

Colors
33a6d7
ffc214

Requirements
Must have
• Why Tollo?
• -Top 5 Questions
• Tollo Certified
• -Graphic detailing inspection
• How it Works
• -Graphic-- 1. Find a Location 2. Personal/Vehicle Info Form 3. Purchase
• -Get a Tollo Inspection
• Get a Tollo Inspection
• -Find a Location
• -Personal/Vehicle info Form
• -Purchase
• Become a Tollo Dealer
• -Form
• -Upload Credentials
• About Us
• Contact Us
• Term & Conditions
• Privacy
• FAQ
• Press
• Social Media
Nice to have
• Customer feedback-Quorra
Should not have
• Not sure

```html
<!DOCTYPE html>
<html lang="en">
<head>
<meta charset="utf-8">
<title>Tollo — Used Car Inspections</title>
<link href="https://fonts.googleapis.com/css2?family=Open+Sans:wght@400;600;700;800&display=swap" rel="stylesheet">
<style>
:root{
  --blue:#33a6d7;
  --blue-deep:#1e8fc2;
  --orange:#f5a01a;
  --yellow:#ffc214;
  --green:#5cb85c;
  --red:#e74c3c;
  --ink:#333a40;
  --muted:#8a9096;
  --line:#e3e6e8;
  --peach:#fcebd9;
  --paper:#ffffff;
  --soft:#f4f5f6;
}
*{box-sizing:border-box;margin:0;padding:0}
html,body{width:1200px;height:2400px;overflow:hidden}
body{font-family:"Open Sans",Arial,sans-serif;color:var(--ink);background:var(--paper);position:relative;font-size:13px}
.abs{position:absolute}

/* header */
.brand{left:40px;top:30px;display:flex;align-items:center;gap:10px;font-size:30px;font-weight:800;color:var(--ink)}
.brand .dot{width:26px;height:26px;border-radius:50%;background:var(--blue)}
.quicklinks{right:30px;top:34px;display:flex;gap:26px;align-items:center;font-size:12px;font-weight:600}
.quicklinks a{display:flex;align-items:center;gap:8px;color:var(--ink);text-decoration:none}
.quicklinks .ico{width:20px;height:20px;border-radius:50%;display:inline-block}
.ico.q{background:var(--blue)} .ico.c{background:var(--orange)} .ico.g{background:var(--green)}
.phone{background:var(--red);color:#fff !important;padding:5px 14px;border-radius:14px}
.mainnav{left:0;top:104px;width:1200px;height:40px;border-top:1px solid var(--line);border-bottom:1px solid var(--line);display:flex;align-items:center;padding:0 100px}
.mainnav a{font-size:12px;font-weight:600;color:var(--ink);text-decoration:none;margin-right:46px}
.search{margin-left:auto;width:210px;height:26px;border:1px solid var(--line);border-radius:13px;display:flex;align-items:center;justify-content:flex-end;padding-right:8px}

/* hero */
.hero-img{left:60px;top:160px;width:560px;height:290px;background:radial-gradient(ellipse at 50% 60%,#7a1f22 0%,#a85a5a 30%,#e9e4e2 62%,#fafafa 100%)}
.hero-copy{left:660px;top:236px;width:480px;text-align:center}
.hero-copy h1{font-size:30px;font-weight:700;color:var(--ink)}
.hero-copy p{font-size:17px;margin-top:10px}
.hero-copy p b{color:var(--orange)}
.btn{display:inline-block;border-radius:22px;font-weight:600;color:#fff;text-decoration:none}
.btn-blue{background:var(--blue);padding:12px 34px;font-size:14px;margin-top:26px}
.dots{display:flex;gap:6px}
.dots i{width:8px;height:8px;border-radius:50%;background:#cfd3d6;display:block}
.dots i.on{background:var(--blue)}

/* buyers / sellers */
.split{left:100px;top:490px;width:1000px;height:200px;display:flex}
.split .side{flex:1;padding:38px 40px}
.split .buyers{background:var(--peach)}
.split .sellers{background:var(--soft);text-align:right}
.split h3{font-size:20px;font-weight:700;letter-spacing:.5px;color:var(--ink)}
.split .buyers h3{color:var(--orange)}
.split p{font-size:12px;color:var(--muted);width:250px;margin-top:8px;line-height:1.6}
.split .sellers p{margin-left:auto}
.circle{top:530px;width:124px;height:124px;border-radius:50%;display:flex;align-items:center;justify-content:center;font-size:24px;font-weight:800;color:#fff}
.circle.buy{left:478px;background:var(--orange);z-index:2}
.circle.sell{left:598px;background:var(--blue)}

/* certified */
.sec-title{left:0;top:752px;width:1200px;text-align:center;font-size:19px;font-weight:800;letter-spacing:1px}
.inspect-art{left:110px;top:810px;width:360px;height:210px;background:radial-gradient(ellipse at 50% 50%,#c8323a 0%,#d98a8d 35%,#e6ebf0 65%,#fff 100%)}
.inspect{left:520px;top:820px;width:580px}
.inspect h4{font-size:16px;font-weight:700}
.inspect p{font-size:12px;color:var(--muted);line-height:1.65;margin-top:10px}
.checks{display:grid;grid-template-columns:1fr 1fr;gap:18px 20px;margin-top:20px;font-size:12px;color:var(--muted)}
.checks li{list-style:none;display:flex;align-items:center;gap:10px}

/* listings */
.arrow{top:1262px;width:30px;height:30px;border-radius:50%;background:#d9dcdf;display:flex;align-items:center;justify-content:center}
.cards{left:100px;top:1112px;width:1000px;display:flex;gap:30px}
.card{flex:1;border:1px solid var(--line);height:330px;padding:14px}
.card .pic{height:150px;background:radial-gradient(ellipse at 50% 60%,#bfc4c8 0%,#e4e7e9 45%,#fff 75%)}
.card .cap{font-size:11px;color:var(--ink);margin-top:16px;text-align:center}
.card .specs{display:flex;justify-content:center;gap:14px;margin-top:16px}
.card .specs i{width:16px;height:16px;border-radius:50%;border:2px solid #c9cdd0;display:block}
.card .acts{display:flex;justify-content:center;gap:10px;margin-top:22px}
.card .acts a{font-size:11px;padding:6px 18px;border-radius:14px;text-decoration:none;color:#fff}
.acts .details{background:#d5d8db}
.acts .more{background:var(--orange)}

/* testimonial */
.story-img{left:100px;top:1510px;width:1000px;height:490px;background:linear-gradient(110deg,#20303a 0%,#4f6470 30%,#c9a48c 55%,#8c9aa3 80%,#d8dee2 100%)}
.quote{left:112px;top:1790px;width:370px;height:196px;background:var(--blue);color:#fff;padding:26px 28px}
.quote .who{font-size:15px;font-weight:700}
.quote .who span{font-size:11px;font-weight:400;margin-left:14px;opacity:.9}
.quote p{font-size:11px;line-height:1.65;margin-top:12px;opacity:.95}

/* footer */
.footer{left:0;top:2040px;width:1200px;height:360px;background:var(--blue);color:#fff}
.fcol{top:46px}
.fcol h5{font-size:14px;font-weight:700;margin-bottom:14px}
.fcol a,.fcol span{display:block;font-size:11px;color:#fff;text-decoration:none;line-height:2}
.news{display:flex;margin-top:4px}
.news .field{width:180px;height:32px;background:#fff;color:#aab;font-size:11px;padding:8px 12px}
.news .go{width:36px;height:32px;background:var(--orange);display:flex;align-items:center;justify-content:center}
.socials{display:flex;gap:10px;margin-top:22px}
.socials i{width:22px;height:22px;border-radius:50%;background:rgba(255,255,255,.85);display:block}
.fbottom{left:100px;top:294px;width:1000px;border-top:1px solid rgba(255,255,255,.4);padding-top:20px;display:flex;align-items:center;font-size:11px}
.cards-pay{margin-left:auto;display:flex;gap:8px}
.cards-pay i{width:36px;height:22px;border-radius:3px;background:#fff;display:block}
</style>
</head>
<body>

<header>
  <div class="abs brand"><span class="dot"></span>Tollo</div>
  <nav class="abs quicklinks">
    <a href="#"><span class="ico q"></span>Top 5 Questions</a>
    <a href="#"><span class="ico c"></span>Tollo Certified</a>
    <a href="#"><span class="ico g"></span>Get an Inspection</a>
    <a href="#" class="phone">000 000 0000</a>
  </nav>
  <nav class="abs mainnav">
    <a href="#">Home</a>
    <a href="#">Why Tollo</a>
    <a href="#">Get a Tollo Report</a>
    <a href="#">Find a Tollo Location</a>
    <a href="#">Be a Tollo Mechanic</a>
    <div class="search">
      <svg width="12" height="12" viewBox="0 0 12 12"><circle cx="5" cy="5" r="3.8" fill="none" stroke="#8a9096" stroke-width="1.5"/><line x1="8" y1="8" x2="11" y2="11" stroke="#8a9096" stroke-width="1.5"/></svg>
    </div>
  </nav>
</header>

<section class="hero">
  <div class="abs hero-img" role="img" aria-label="Photo of a classic red car on a white background"></div>
  <div class="abs hero-copy">
    <h1>Find A Tollo Used Car</h1>
    <p>Get a <b>Tollo</b> Used Car Inspection</p>
    <a href="#" class="btn btn-blue">Get a Tollo Inspection</a>
  </div>
  <div class="abs dots" style="left:582px;top:440px"><i class="on"></i><i></i><i></i></div>
</section>

<section class="abs split">
  <div class="side buyers">
    <h3>BUYERS</h3>
    <p>Buying used? Get every car checked by an expert before you pay, so you drive away sure.</p>
  </div>
  <div class="side sellers">
    <h3>SELLERS</h3>
    <p>Show buyers your car is sound with a Tollo report they can trust.</p>
  </div>
</section>
<div class="abs circle buy">BUY</div>
<div class="abs circle sell">SELL</div>

<h2 class="abs sec-title">TOLLO CERTIFIED</h2>

<section>
  <div class="abs inspect-art" role="img" aria-label="Illustration of a red car with its parts laid out around it"></div>
  <div class="abs inspect">
    <h4>Tollo Inspection Details</h4>
    <p>Every Tollo inspection covers the engine, brakes, body, electrics and road test. Our certified mechanics check over one hundred points and send you a clear report the same day, with photos and notes on anything that needs attention before you buy.</p>
    <ul class="checks">
      <li><svg width="18" height="18" viewBox="0 0 18 18"><circle cx="9" cy="9" r="9" fill="var(--blue)"/><path d="M5 9l3 3 5-6" stroke="#fff" stroke-width="2" fill="none"/></svg>Engine and gearbox check</li>
      <li><svg width="18" height="18" viewBox="0 0 18 18"><circle cx="9" cy="9" r="9" fill="var(--blue)"/><path d="M5 9l3 3 5-6" stroke="#fff" stroke-width="2" fill="none"/></svg>Brakes and suspension test</li>
      <li><svg width="18" height="18" viewBox="0 0 18 18"><circle cx="9" cy="9" r="9" fill="var(--blue)"/><path d="M5 9l3 3 5-6" stroke="#fff" stroke-width="2" fill="none"/></svg>Body and rust review</li>
      <li><svg width="18" height="18" viewBox="0 0 18 18"><circle cx="9" cy="9" r="9" fill="var(--blue)"/><path d="M5 9l3 3 5-6" stroke="#fff" stroke-width="2" fill="none"/></svg>Road test with full report</li>
    </ul>
  </div>
</section>

<section>
  <div class="abs arrow" style="left:18px"><svg width="10" height="10" viewBox="0 0 10 10"><path d="M7 1L3 5l4 4" stroke="#fff" stroke-width="2" fill="none"/></svg></div>
  <div class="abs arrow" style="left:1152px"><svg width="10" height="10" viewBox="0 0 10 10"><path d="M3 1l4 4-4 4" stroke="#fff" stroke-width="2" fill="none"/></svg></div>
  <div class="abs cards">
    <article class="card">
      <div class="pic" role="img" aria-label="Photo of a silver hatchback"></div>
      <div class="cap">2016 Arvan KT5 4dr Sedan | 27,200 miles</div>
      <div class="specs"><i></i><i></i><i></i><i></i><i></i></div>
      <div class="acts"><a href="#" class="details">Details</a><a href="#" class="more">Read More</a></div>
    </article>
    <article class="card">
      <div class="pic" role="img" aria-label="Photo of a silver sedan"></div>
      <div class="cap">2016 Arvan KT5 4dr Sedan | 27,200 miles</div>
      <div class="specs"><i></i><i></i><i></i><i></i><i></i></div>
      <div class="acts"><a href="#" class="details">Details</a><a href="#" class="more">Read More</a></div>
    </article>
    <article class="card">
      <div class="pic" role="img" aria-label="Photo of a white sedan"></div>
      <div class="cap">2016 Arvan KT5 4dr Sedan | 27,200 miles</div>
      <div class="specs"><i></i><i></i><i></i><i></i><i></i></div>
      <div class="acts"><a href="#" class="details">Details</a><a href="#" class="more">Read More</a></div>
    </article>
  </div>
</section>

<section>
  <div class="abs story-img" role="img" aria-label="Photo of a happy customer in her car holding up the keys"></div>
  <div class="abs quote">
    <div class="who">Dara Collins<span>Tollo customer</span></div>
    <p>I had the car inspected before buying and the report found a brake issue. The seller fixed it and I drove home with total peace of mind. I will use Tollo again.</p>
  </div>
  <div class="abs dots" style="left:582px;top:1970px"><i class="on"></i><i></i><i></i></div>
</section>

<footer class="abs footer">
  <div class="abs fcol" style="left:100px">
    <h5>Sitemap</h5>
    <a href="#">Home</a><a href="#">Car</a><a href="#">Who Us</a><a href="#">Terms</a><a href="#">Forward Events</a>
  </div>
  <div class="abs fcol" style="left:290px">
    <h5>Support</h5>
    <a href="#">Get Started</a><a href="#">Sign In</a><a href="#">Help</a><a href="#">List A car</a>
  </div>
  <div class="abs fcol" style="left:500px">
    <h5>Address</h5>
    <span>14 Harbour Lane</span><span>Riverton 3100</span><span>+1 (555) 014 2290</span><span>hello@tollomail.com</span>
  </div>
  <div class="abs fcol" style="left:810px">
    <h5>Subscribe to our newsletter</h5>
    <div class="news"><div class="field">Enter email</div><div class="go"><svg width="12" height="12" viewBox="0 0 12 12"><path d="M1 6h9M6 2l4 4-4 4" stroke="#fff" stroke-width="2" fill="none"/></svg></div></div>
    <div class="socials"><i></i><i></i><i></i><i></i><i></i><i></i></div>
  </div>
  <div class="abs fbottom">
    <span>tollo © 2015 All Rights Reserved</span>
    <div class="cards-pay"><i></i><i></i><i></i><i></i></div>
  </div>
</footer>

</body>
</html>
```